Hargrove - Pellman Corporate PowerPoint Presentation Template

A custom, corporate template that is highly professional, neat/crisp, "serious," and captures/emphasizes the essence of a global, mutli-brand consumer products company that has deep tradition and values family, hard work, performance, innovation, and service to our consumers and retail partners.
The company's roots and headquarters are in Texas. We are a private and family owned since our founding almost 100 years ago. The corporate website is www.hpxcorp.example and other branded websites can be accessed from this site.
Our current presentation title page is attached. We believe it to be somewhat stale/out of date and less sophisticated that the image we'd prefer to project. We occasionally add/change logos and will have to adapt the presentation. These presentations must look good printed.
Please contact me with any questions or requests and I will respond very quickly.
Corporate Executives
It Professional
- Sans Serif font (can't select below). Industry is Apparel and Footwear / Consumer Products (can't select below).

```html
<!DOCTYPE html>
<html lang="en">
<head>
<meta charset="utf-8">
<title>Hargrove - Pellman Corporate Presentation Template</title>
<link href="https://fonts.googleapis.com/css2?family=Open+Sans:ital,wght@0,400;0,600;0,700;1,400&display=swap" rel="stylesheet">
<style>
:root{
  --board:#6b6b6d;
  --blue:#1451a6;
  --blue-dark:#0f3f85;
  --red:#d8213b;
  --yellow:#fbd200;
  --grey:#bdbdbd;
  --ink:#555;
  --muted:#999;
  --rule:#9aa3b5;
  --paper:#ffffff;
  --head:#f4f4f4;
}
*{box-sizing:border-box;margin:0;padding:0}
html,body{width:1200px;height:1200px;overflow:hidden;background:var(--board);font-family:"Open Sans",Arial,sans-serif}
.board{position:relative;width:1200px;height:1200px}
.slide{position:absolute;width:368px;height:276px;background:var(--paper);overflow:hidden}
.c1{left:30px}.c2{left:412px}.c3{left:798px}
.r1{top:28px}.r2{top:319px}.r3{top:611px}.r4{top:904px}
.head{position:absolute;left:0;top:0;width:100%;height:44px;background:var(--head);border-bottom:1px solid #e2e2e2}
.brand{position:absolute;display:flex;align-items:center;gap:3px;font-weight:700;color:var(--blue);font-size:6.4px;letter-spacing:.2px;white-space:nowrap}
.brand .mark{width:7px;height:7px;background:var(--blue)}
.head .brand{left:12px;top:18px}
.title{position:absolute;right:34px;top:9px;text-align:right;color:var(--blue);font-size:12.5px;line-height:15px}
.title small{display:block;color:var(--muted);font-size:5px;line-height:8px}
.foot{position:absolute;left:0;bottom:9px;width:100%;height:6px}
.foot::before,.foot::after{content:"";position:absolute;left:0;right:40px;border-top:1px dashed var(--rule)}
.foot::before{top:0}.foot::after{top:4px}
.foot .edge{position:absolute;right:0;top:0;width:16px;height:6px;border-top:1px dashed var(--rule);border-bottom:1px dashed var(--rule)}
.foot .num{position:absolute;right:26px;top:-2px;font-size:4.5px;color:#333}
.copy{position:absolute;font-size:4.2px;line-height:7px;color:var(--ink);text-align:justify}
.photo{position:absolute}
/* slide 1 */
.welcome{background:var(--blue)}
.welcome .hero{position:absolute;left:0;top:0;width:100%;height:150px}
.welcome .brand{right:18px;top:38px;color:#fff}
.welcome .brand .mark{background:#fff}
.welcome .greet{position:absolute;right:34px;top:160px;text-align:right;color:#fff}
.greet h1{font-size:14px;font-weight:600;line-height:16px}
.greet p{font-size:11px;line-height:14px}
.greet span{font-size:6.5px}
.dash-w{position:absolute;left:0;right:0;border-top:1px dashed rgba(255,255,255,.7)}
.legal{position:absolute;left:140px;bottom:10px;font-size:3px;color:#fff}
/* slide 2 */
.stitch-band{position:absolute;left:0;top:64px;width:100%;height:13px;background:var(--blue);border-top:2px solid #fff;outline:1px dashed #fff;outline-offset:-5px}
.quote{position:absolute;left:28px;top:116px;width:150px;font-size:6.8px;line-height:9.5px;font-style:italic;color:#223}
/* leadership */
.people{position:absolute;left:24px;top:112px;display:flex;gap:12px}
.person{width:55px}
.person .pic{height:62px;background:#e0e0e0;border-radius:0 8px 0 0}
.person h4{margin-top:9px;text-align:center;font-size:5.8px;color:var(--blue);line-height:7px}
.person h5{text-align:center;font-size:4px;color:#333;font-style:italic;font-weight:600}
.person p{font-size:3.4px;line-height:5px;color:var(--ink);text-align:center}
/* brands */
.brands{position:absolute;left:28px;top:118px;width:320px}
.brands .row{display:flex;align-items:center;justify-content:space-between;height:48px}
.bn{font-weight:700;font-size:15px;letter-spacing:.3px}
.bn.s{display:flex;align-items:center;gap:3px}
.bn .sq{width:9px;height:9px}
/* section */
.section{background:#2c4f86}
.section .circle{position:absolute;left:129px;top:89px;width:112px;height:112px;border-radius:50%;background:#fff;border:4px solid #c9d6ea;display:flex;align-items:center;justify-content:center}
.section .circle .brand{position:static;font-size:8px}
.section .stitle{position:absolute;right:18px;bottom:28px;color:#fff;font-size:11.5px}
/* table */
.tbl{position:absolute;left:28px;top:81px;width:313px;border-collapse:collapse;font-size:5.8px;text-align:center}
.tbl th{background:var(--blue);color:#fff;font-weight:400;height:18px;border-right:1px solid #fff}
.tbl td{height:20px;color:#aaa;font-size:5.2px}
.tbl tr.alt td{background:#d6e3f3}
.tbl tr.alt td:first-child{background:#e3e8ef}
/* charts */
.chart{position:absolute;left:20px;top:62px}
.ax{font-size:4.2px;fill:#666;font-family:"Open Sans",Arial,sans-serif}
.pct{font-weight:600;font-family:"Open Sans",Arial,sans-serif}
/* two column */
.col{position:absolute;top:76px;width:150px}
.col h3{font-size:7px;color:var(--blue);font-weight:700;margin-bottom:4px}
.col p{font-size:4px;line-height:5.6px;color:var(--ink);text-align:justify;margin-bottom:6px}
/* thanks */
.thanks{background:#ececee}
.thanks .brand{left:140px;top:104px;font-size:9.5px}
.thanks .brand .mark{width:9px;height:9px}
.thanks h2{position:absolute;left:0;width:100%;top:160px;text-align:center;padding-left:46px;color:var(--blue);font-size:15px;font-weight:600}
.thanks .bar{position:absolute;left:0;bottom:0;width:100%;height:11px;background:var(--blue);color:#fff;font-size:4.5px;text-align:right;padding:3px 24px 0 0}
.dash-b{position:absolute;left:0;right:0;border-top:1px dashed var(--rule)}
</style>
</head>
<body>
<main class="board">

<!-- 1 Welcome -->
<section class="slide welcome c1 r1">
  <svg class="hero" viewBox="0 0 368 150" preserveAspectRatio="none" role="img" aria-label="Photo of a worker in gloves grinding metal with sparks flying">
    <defs><linearGradient id="heroG" x1="0" y1="0" x2="1" y2="1"><stop offset="0" stop-color="#2a2f3a"/><stop offset=".5" stop-color="#8a5a2a"/><stop offset="1" stop-color="#3a3c44"/></linearGradient></defs>
    <polygon points="0,0 368,0 368,88 180,122 0,90" fill="url(#heroG)"/>
  </svg>
  <div class="brand"><span class="mark"></span>HARGROVE-PELLMAN</div>
  <div class="greet"><h1>WELCOME</h1><p>TO OUR PRESENTATION</p><span>January 2016</span></div>
  <div class="dash-w" style="top:240px"></div><div class="dash-w" style="top:244px"></div>
  <div class="legal">© 2016 Hargrove-Pellman Co. Proprietary &amp; Confidential</div>
</section>

<!-- 2 Values & Vision -->
<section class="slide c2 r1">
  <header class="head"><div class="brand"><span class="mark"></span>HARGROVE-PELLMAN</div><div class="title">Values &amp; Vision<small>Lorem ipsum dolor sit amet consectetur</small></div></header>
  <div class="stitch-band"></div>
  <div class="photo" style="left:0;top:79px;width:368px;height:112px;background:linear-gradient(100deg,#c9ccd6 0%,#3d4760 45%,#1c2438 100%)" role="img" aria-label="Photo of a sewing machine stitching dark fabric"></div>
  <p class="quote">“Lorem ipsum dolor sit amet, consectetur adipiscing elit. Praesent sodales odio consectetur adipiscing elit. Lorem ipsum dolor sit amet, consectetur g elit.”</p>
  <p class="copy" style="left:28px;top:204px;width:314px">Lorem ipsum dolor sit amet, consectetur adipiscing elit. Praesent sodales odio sit amet odio tristique quis tempus odio lorem ipsum dolor sit amet, consectetur adipiscing elit. Lorem ipsum dolor sit amet, consectetur adipiscing elit. Praesent sodales odio sit amet odio tristique quis tempus odio lorem ipsum dolor sit amet, consectetur adipiscing elit. Lorem ipsum dolor sit amet, consectetur adipiscing elit. Praesent sodales odio sit amet odio tristique quis tempus odio lorem ipsum dolor sit amet. Lorem ipsum dolor sit amet, consectetur adipiscing elit. Praesent sodales odio sit amet odio tristique quis tempus odio.</p>
  <div class="foot"><span class="num">1</span><span class="edge"></span></div>
</section>

<!-- 3 Leadership -->
<section class="slide c3 r1">
  <header class="head"><div class="brand"><span class="mark"></span>HARGROVE-PELLMAN</div><div class="title">Leadership<small>Lorem ipsum dolor sit amet consectetur</small></div></header>
  <p class="copy" style="left:24px;top:70px;width:322px">Hargrove-Pellman Manufacturing Company is a global organization deeply rooted in providing trusted, quality workwear at an unmatched value. My family started this company in 1922 with a single goal in mind: to meet the needs of a growing American workforce by making superior, durable workwear at an affordable price, with a satisfaction guarantee to our customers. Our commitment to our customers is something from which we will never waiver.</p>
  <div class="people">
    <div class="person"><div class="pic"></div><h4>JHON DOE</h4><h5>Manager</h5><p>Lorem ipsum dolor sit amet, consectetur praesent sodales odio sit amet lorem ipsum dolor sit amet, tristique quis tempus.</p></div>
    <div class="person"><div class="pic"></div><h4>JHON DOE</h4><h5>Manager</h5><p>Lorem ipsum dolor sit amet, consectetur praesent sodales odio sit amet lorem ipsum dolor sit amet, tristique quis tempus.</p></div>
    <div class="person"><div class="pic"></div><h4>JHON DOE</h4><h5>Manager</h5><p>Lorem ipsum dolor sit amet, consectetur praesent sodales odio sit amet lorem ipsum dolor sit amet, tristique quis tempus.</p></div>
    <div class="person"><div class="pic"></div><h4>JHON DOE</h4><h5>Manager</h5><p>Lorem ipsum dolor sit amet, consectetur praesent sodales odio sit amet lorem ipsum dolor sit amet, tristique quis tempus.</p></div>
    <div class="person"><div class="pic"></div><h4>JHON DOE</h4><h5>Manager</h5><p>Lorem ipsum dolor sit amet, consectetur praesent sodales odio sit amet lorem ipsum dolor sit amet, tristique quis tempus.</p></div>
  </div>
  <div class="foot"><span class="num">2</span><span class="edge"></span></div>
</section>

<!-- 4 Global, Multi-Brand -->
<section class="slide c1 r2">
  <header class="head"><div class="brand"><span class="mark"></span>HARGROVE-PELLMAN</div><div class="title">Global, Mutli-Brand<small>Lorem ipsum dolor sit amet consectetur</small></div></header>
  <div class="photo" style="left:150px;top:30px;width:250px;height:230px;border-radius:50%;background:radial-gradient(circle,#f1f4f8 0%,#fff 70%)" role="img" aria-label="Faint world globe backdrop"></div>
  <p class="copy" style="left:33px;top:68px;width:303px">Hargrove-Pellman Manufacturing Company is a global organization deeply rooted in providing trusted, quality workwear at an unmatched value. My family started this company in 1922 with a single goal in mind: to meet the needs of a growing American workforce by making superior, durable workwear at an affordable price, with a satisfaction guarantee to our customers. Our commitment to our customers is something from which we will never waiver.</p>
  <div class="brands">
    <div class="row">
      <span class="bn" style="color:var(--blue)">Dunmore</span>
      <span class="bn" style="color:#e8532a">Wexley</span>
      <span class="bn" style="color:#222">TARROW</span>
      <span class="bn s" style="color:var(--red)"><span class="sq" style="background:var(--yellow)"></span>JOB STANDARD</span>
    </div>
    <div class="row" style="justify-content:flex-start;gap:28px">
      <span class="bn" style="color:#222">WORTHLINE</span>
      <span class="bn" style="color:var(--red)">KESTREL</span>
      <span class="bn" style="color:var(--blue)">NORVIK</span>
    </div>
  </div>
  <div class="foot"><span class="num">3</span><span class="edge"></span></div>
</section>

<!-- 5 Section -->
<section class="slide section c2 r2">
  <div class="photo" style="inset:0;background:linear-gradient(135deg,#1d3a6a 0%,#3d6398 50%,#223f72 100%)" role="img" aria-label="Blue-tinted photo of a gloved worker with a grinder"></div>
  <div class="circle"><div class="brand"><span class="mark"></span>HARGROVE-PELLMAN</div></div>
  <div class="stitle">Section Title</div>
</section>

<!-- 6 Table -->
<section class="slide c3 r2">
  <header class="head"><div class="brand"><span class="mark"></span>HARGROVE-PELLMAN</div><div class="title">Table Slide<small>Lorem ipsum dolor sit amet consectetur</small></div></header>
  <table class="tbl">
    <tr><th>Lorem ipsum</th><th>Lorem ipsum</th><th>Lorem ipsum</th><th>Lorem ipsum</th></tr>
    <tr><td>sample text</td><td>sample text</td><td>sample text</td><td>sample text</td></tr>
    <tr class="alt"><td>sample text</td><td>sample text</td><td>sample text</td><td>sample text</td></tr>
    <tr><td>sample text</td><td>sample text</td><td>sample text</td><td>sample text</td></tr>
    <tr class="alt"><td>sample text</td><td>sample text</td><td>sample text</td><td>Lorem ipsum</td></tr>
    <tr><td>sample text</td><td>sample text</td><td>sample text</td><td>Lorem ipsum</td></tr>
  </table>
  <p class="copy" style="left:32px;top:213px;width:308px;color:#8a9bc4;font-size:3.8px;line-height:5px">Lorem ipsum dolor sit amet, consectetur adipiscing elit. Praesent sodales odio sit amet odio tristique quis tempus odio lorem ipsum dolor sit amet, consectetur adipiscing elit. Lorem ipsum dolor sit amet, consectetur adipiscing elit. Praesent sodales odio sit amet odio tristique quis tempus odio lorem ipsum dolor sit amet, consectetur adipiscing elit.</p>
  <div class="foot"><span class="num">8</span><span class="edge"></span></div>
</section>

<!-- 7 Bar chart -->
<section class="slide c1 r3">
  <header class="head"><div class="brand"><span class="mark"></span>HARGROVE-PELLMAN</div><div class="title">Chart Slide<small>Lorem ipsum dolor sit amet consectetur</small></div></header>
  <svg class="chart" width="330" height="135" viewBox="0 0 330 135">
    <g class="ax" text-anchor="end">
      <text x="10" y="121">0</text><text x="10" y="106">10</text><text x="10" y="91">20</text><text x="10" y="76">30</text><text x="10" y="61">40</text><text x="10" y="46">50</text><text x="10" y="31">60</text><text x="10" y="16">70</text>
    </g>
    <line x1="15" y1="119" x2="300" y2="119" stroke="#ccc" stroke-width=".6"/>
    <line x1="15" y1="14" x2="15" y2="119" stroke="#ccc" stroke-width=".6"/>
    <g>
      <rect x="22" y="71" width="9" height="48" fill="var(--yellow)"/><rect x="31" y="81.5" width="9" height="37.5" fill="var(--grey)"/><rect x="40" y="96.5" width="9" height="22.5" fill="var(--blue)"/><rect x="49" y="101" width="9" height="18" fill="var(--red)"/>
      <rect x="79" y="71" width="9" height="48" fill="var(--yellow)"/><rect x="88" y="66.5" width="9" height="52.5" fill="var(--grey)"/><rect x="97" y="84.5" width="9" height="34.5" fill="var(--blue)"/><rect x="106" y="101" width="9" height="18" fill="var(--red)"/>
      <rect x="136" y="77" width="9" height="42" fill="var(--yellow)"/><rect x="145" y="89" width="9" height="30" fill="var(--grey)"/><rect x="154" y="29" width="9" height="90" fill="var(--blue)"/><rect x="163" y="101" width="9" height="18" fill="var(--red)"/>
      <rect x="193" y="101" width="9" height="18" fill="var(--yellow)"/><rect x="202" y="74" width="9" height="45" fill="var(--grey)"/><rect x="211" y="47" width="9" height="72" fill="var(--blue)"/><rect x="220" y="87.5" width="9" height="31.5" fill="var(--red)"/>
      <rect x="250" y="96.5" width="9" height="22.5" fill="var(--yellow)"/><rect x="259" y="80" width="9" height="39" fill="var(--grey)"/><rect x="268" y="41" width="9" height="78" fill="var(--blue)"/><rect x="277" y="77" width="9" height="42" fill="var(--red)"/>
    </g>
    <g class="ax" text-anchor="middle" style="font-size:3.4px">
      <text x="40" y="126">5/1/2015</text><text x="97" y="126">6/1/2015</text><text x="154" y="126">7/1/2015</text><text x="211" y="126">8/1/2015</text><text x="268" y="126">9/1/2015</text>
    </g>
    <g class="ax" style="font-size:3.4px">
      <rect x="312" y="56" width="5" height="4" fill="var(--blue)"/><text x="320" y="59.5">Indonesia</text>
      <rect x="312" y="70" width="5" height="4" fill="var(--yellow)"/><text x="320" y="73.5">Indonesia</text>
      <rect x="312" y="84" width="5" height="4" fill="var(--red)"/><text x="320" y="87.5">Indonesia</text>
      <rect x="312" y="98" width="5" height="4" fill="var(--grey)"/><text x="320" y="101.5">Indonesia</text>
    </g>
  </svg>
  <p class="copy" style="left:27px;top:210px;width:316px;font-size:3.8px;line-height:9px;color:#667">Lorem ipsum dolor sit amet, <i><b>consectetur adipiscing elit.</b></i> Praesent sodales odio sit amet odio tristique quis tempus odio lorem ipsum dolor sit amet, consectetur adipiscing elit. Lorem ipsum dolor sit amet, consectetur adipiscing elit. Praesent sodales odio sit amet odio tristique quis tempus odio lorem ipsum dolor sit amet, consectetur adipiscing elit. Lorem ipsum dolor sit amet, consectetur adipiscing elit.</p>
  <div class="foot"><span class="num">5</span><span class="edge"></span></div>
</section>

<!-- 8 Line chart -->
<section class="slide c2 r3">
  <header class="head"><div class="brand"><span class="mark"></span>HARGROVE-PELLMAN</div><div class="title">Chart Slide<small>Lorem ipsum dolor sit amet consectetur</small></div></header>
  <svg class="chart" width="340" height="140" viewBox="0 0 340 140" style="left:14px;top:54px">
    <g stroke="#ddd" stroke-width=".6">
      <line x1="30" y1="8" x2="295" y2="8"/><line x1="30" y1="28" x2="295" y2="28"/><line x1="30" y1="48" x2="295" y2="48"/><line x1="30" y1="68" x2="295" y2="68"/><line x1="30" y1="88" x2="295" y2="88"/><line x1="30" y1="108" x2="295" y2="108"/><line x1="30" y1="128" x2="295" y2="128"/>
      <line x1="30" y1="8" x2="30" y2="128"/>
    </g>
    <g class="ax" text-anchor="end" style="font-size:5px">
      <text x="24" y="130">0</text><text x="24" y="110">1</text><text x="24" y="90">2</text><text x="24" y="70">3</text><text x="24" y="50">4</text><text x="24" y="30">5</text><text x="24" y="10">6</text>
    </g>
    <polyline points="63,42 126,78 189,58 252,38" fill="none" stroke="var(--blue)" stroke-width="1"/>
    <polyline points="63,80 126,40 189,92 252,72" fill="none" stroke="var(--red)" stroke-width="1"/>
    <polyline points="63,88 126,88 189,68 252,28" fill="none" stroke="var(--grey)" stroke-width="1"/>
    <g class="ax" text-anchor="middle"><text x="63" y="137">Category 1</text><text x="126" y="137">Category 2</text><text x="189" y="137">Category 3</text><text x="252" y="137">Category 4</text></g>
    <g class="ax">
      <line x1="300" y1="59" x2="308" y2="59" stroke="var(--blue)"/><text x="310" y="61">Series 1</text>
      <line x1="300" y1="69" x2="308" y2="69" stroke="var(--red)"/><text x="310" y="71">Series 2</text>
      <line x1="300" y1="79" x2="308" y2="79" stroke="var(--grey)"/><text x="310" y="81">Series 3</text>
    </g>
  </svg>
  <p class="copy" style="left:27px;top:210px;width:316px;font-size:3.8px;line-height:9px;color:#667">Lorem ipsum dolor sit amet, <i><b>consectetur adipiscing elit.</b></i> Praesent sodales odio sit amet odio tristique quis tempus odio lorem ipsum dolor sit amet, consectetur adipiscing elit. Lorem ipsum dolor sit amet, consectetur adipiscing elit. Praesent sodales odio sit amet odio tristique quis tempus odio lorem ipsum dolor sit amet, consectetur adipiscing elit. Lorem ipsum dolor sit amet, consectetur adipiscing elit.</p>
  <div class="foot"><span class="num">6</span><span class="edge"></span></div>
</section>

<!-- 9 Pie chart -->
<section class="slide c3 r3">
  <header class="head"><div class="brand"><span class="mark"></span>HARGROVE-PELLMAN</div><div class="title">Bi Chart Slide<small>Lorem ipsum dolor sit amet consectetur</small></div></header>
  <svg class="chart" width="330" height="140" viewBox="0 0 330 140" style="left:20px;top:60px">
    <g transform="translate(20,22) scale(1.0)">
      <path d="M50 50 L50 2 A48 48 0 0 1 78.2 88.8 Z" fill="var(--blue)" stroke="#fff" stroke-width=".8"/>
      <path d="M50 50 L78.2 88.8 A48 48 0 0 1 11.2 78.2 Z" fill="var(--yellow)" stroke="#fff" stroke-width=".8"/>
      <path d="M50 50 L11.2 78.2 A48 48 0 0 1 11.2 21.8 Z" fill="#c4c4c4" stroke="#fff" stroke-width=".8"/>
      <path d="M50 50 L11.2 21.8 A48 48 0 0 1 50 2 Z" fill="var(--red)" stroke="#fff" stroke-width=".8"/>
      <g class="pct" fill="#fff" font-size="5.5"><text x="70" y="55">40%</text><text x="40" y="75">25%</text><text x="7" y="53">20%</text><text x="23" y="22">15%</text></g>
    </g>
    <g fill="none" stroke="#999" stroke-width=".4" stroke-dasharray="1 1">
      <polyline points="64,16 110,16 150,12"/><polyline points="92,40 130,42 150,44"/><polyline points="112,74 130,74 150,74"/><polyline points="80,108 150,108"/>
    </g>
    <g class="pct" font-size="12">
      <text x="158" y="16" fill="#bbb">20%</text><text x="158" y="48" fill="var(--red)">15%</text><text x="158" y="78" fill="var(--blue)">40%</text><text x="158" y="112" fill="#f0a800">25%</text>
    </g>
    <g class="ax" style="font-size:3.6px">
      <text x="198" y="7" font-weight="700" fill="#aaa">Title Goes Here</text><text x="198" y="13">There are many variations of passages of</text><text x="198" y="18">Lorem Ipsum available.</text>
      <text x="198" y="39" font-weight="700" fill="var(--red)">Title Goes Here</text><text x="198" y="45">There are many variations of passages of</text><text x="198" y="50">Lorem Ipsum available.</text>
      <text x="198" y="69" font-weight="700" fill="var(--blue)">Title Goes Here</text><text x="198" y="75">There are many variations of passages of</text><text x="198" y="80">Lorem Ipsum available.</text>
      <text x="198" y="103" font-weight="700" fill="#f0a800">Title Goes Here</text><text x="198" y="109">There are many variations of passages of</text><text x="198" y="114">Lorem Ipsum available.</text>
    </g>
  </svg>
  <p class="copy" style="left:27px;top:210px;width:316px;font-size:3.8px;line-height:9px;color:#667">Lorem ipsum dolor sit amet, <i><b>consectetur adipiscing elit.</b></i> Praesent sodales odio sit amet odio tristique quis tempus odio lorem ipsum dolor sit amet, consectetur adipiscing elit. Lorem ipsum dolor sit amet, consectetur adipiscing elit. Praesent sodales odio sit amet odio tristique quis tempus odio lorem ipsum dolor sit amet, consectetur adipiscing elit. Lorem ipsum dolor sit amet, consectetur adipiscing elit.</p>
  <div class="foot"><span class="num">7</span><span class="edge"></span></div>
</section>

<!-- 10 Global presence -->
<section class="slide c1 r4">
  <header class="head"><div class="brand"><span class="mark"></span>HARGROVE-PELLMAN</div><div class="title">Global Presence<small>Lorem ipsum dolor sit amet consectetur</small></div></header>
  <div class="photo" style="left:70px;top:74px;width:250px;height:130px;border-radius:40% 45% 30% 35%;background:radial-gradient(ellipse at center,#1c57a8 0%,#1451a6 55%,#dfe7f3 72%,#fff 80%)" role="img" aria-label="World map in blue with red and yellow markers showing company locations"></div>
  <svg style="position:absolute;left:36px;top:138px" width="50" height="30" viewBox="0 0 50 30">
    <rect x="0" y="0" width="12" height="6" fill="var(--red)"/><text x="16" y="5" class="ax" style="font-size:3.6px">Area 100%</text>
    <rect x="0" y="15" width="12" height="6" fill="var(--yellow)"/><text x="16" y="20" class="ax" style="font-size:3.6px">Area 100%</text>
  </svg>
  <p class="copy" style="left:30px;top:214px;width:312px;color:#334">Hargrove-Pellman fuels our global growth by focusing on product excellence and maintaining a tireless dedication to superior performance. To secure our position as a global leader in full-service workwear solutions, and to accommodate growing global demand, we’ve established a multi-continent presence and global distribution capabilities. We’ve also leveraged strategic partnerships and acquired companies known for product innovation and excellence in workwear: Alder Crest, Worthline, Kestrel and Tarrow.</p>
  <div class="foot"><span class="num">9</span><span class="edge"></span></div>
</section>

<!-- 11 Two column -->
<section class="slide c2 r4">
  <header class="head"><div class="brand"><span class="mark"></span>HARGROVE-PELLMAN</div><div class="title">Two Column text<small>Lorem ipsum dolor sit amet consectetur</small></div></header>
  <div class="col" style="left:26px">
    <h3>Title Goes Here</h3>
    <p>There are many variations of passages of lorem ipsum available, but the majority have suffered alteration in some form, by injected humour, or randomised words which don't look even slightly believable. If you are going to use a passage of lorem ipsum, you need to be sure there isn't anything embarrassing hidden in the middle of text.</p>
    <p>If you are going to use a passage of lorem ipsum, you need to be sure there isn't anything embarrassing hidden in the middle of text. All the generators on the internet tend to repeat predefined chunks as necessary.</p>
    <p>It uses a dictionary of over 200 Latin words, combined with a handful of model sentence structures, to generate lorem ipsum which looks reasonable. The text is therefore always free from repetition.</p>
    <p>It uses a dictionary of over 200 Latin words, combined with a handful of model sentence structures, to generate lorem ipsum which looks reasonable.</p>
  </div>
  <div class="col" style="left:192px">
    <h3>Title Goes Here</h3>
    <p>There are many variations of passages of lorem ipsum available, but the majority have suffered alteration in some form, by injected humour, or randomised words which don't look even slightly believable. If you are going to use a passage of lorem ipsum, you need to be sure there isn't anything embarrassing hidden in the middle of text.</p>
    <p>If you are going to use a passage of lorem ipsum, you need to be sure there isn't anything embarrassing hidden in the middle of text. All the generators on the internet tend to repeat predefined chunks as necessary.</p>
    <p>It uses a dictionary of over 200 Latin words, combined with a handful of model sentence structures, to generate lorem ipsum which looks reasonable. The text is therefore always free from repetition.</p>
    <p>It uses a dictionary of over 200 Latin words, combined with a handful of model sentence structures, to generate lorem ipsum which looks reasonable.</p>
  </div>
  <div class="foot"><span class="num">11</span><span class="edge"></span></div>
</section>

<!-- 12 Thanks -->
<section class="slide thanks c3 r4">
  <div class="photo" style="inset:0;background:linear-gradient(120deg,#f2f2f3 0%,#d9dbe0 50%,#eeeef0 100%)" role="img" aria-label="Faded photo of a sewing machine stitching fabric"></div>
  <div class="dash-b" style="top:22px"></div><div class="dash-b" style="top:26px"></div>
  <div class="brand"><span class="mark"></span>HARGROVE-PELLMAN</div>
  <h2>THANKS FOR WATCHING</h2>
  <div class="dash-b" style="top:250px"></div><div class="dash-b" style="top:254px"></div>
  <div class="bar">www.hpxcorp.example</div>
</section>

</main>
</body>
</html>
```